Gluten Cove - cover photos - facebooks groups

I have a logo - gluten cove. I have 2 groups that I need cover photos for with the new brand.

Gluten Cove - All Inclusive Reviews

Gluten Cove - Travel Deals

Two separate groups *powered by Journey Crest* at the bottom of the travel deals in fine print. Not the all inclusive group - that’s powered by 2 agencies - at the bottom powered by 2 Brightway Travel Agents.

I want to keep with the current theme. Maybe the logo, and colour dark block on the left (or whatever standard format to make more going forward) then the versions: deals and all inclusive reviews to the right. Happy, simple, clean. Not cheesy. Match the brand and logo to the group.

Attached are the two current cover photos. (To peach!!) I want the pictures and brand to align with the logo. Happy beach - all inclusive. And international travel and fancy cruise for the travel deals.

I’d like a corporate look that we can scale with any new launch.

Thanks!

```html
<!DOCTYPE html>
<html lang="en">
<head>
<meta charset="utf-8">
<title>Gluten Cove – Group Cover Photos</title>
<link rel="stylesheet" href="https://fonts.googleapis.com/css2?family=Montserrat:wght@500;600&family=Poppins:wght@700&display=swap">
<style>
  :root {
    --page: #ffffff;
    --navy: #172a3f;
    --deals-badge: #2e5a7c;
    --reviews-badge: #213f5c;
    --sand-light: #b08a5c;
    --sand-dark: #86663f;
    --white: #ffffff;
    --fine-print: #7f9bb8;
  }
  * { margin: 0; padding: 0; box-sizing: border-box; }
  html, body {
    width: 1200px;
    height: 1200px;
    overflow: hidden;
    background: var(--page);
  }
  .board {
    position: relative;
    width: 1200px;
    height: 1200px;
  }
  .cover {
    position: absolute;
    left: 157px;
    width: 877px;
    height: 483px;
    background: var(--navy);
    overflow: hidden;
  }
  .cover--deals { top: 74px; }
  .cover--reviews { top: 623px; }

  .cover__scene {
    position: absolute;
    inset: 0;
    width: 877px;
    height: 483px;
  }
  .brand {
    position: absolute;
    left: 60px;
    top: 200px;
    width: 160px;
    display: flex;
    flex-direction: column;
    align-items: center;
    gap: 12px;
  }
  .brand__dot {
    width: 54px;
    height: 54px;
    border: 2px solid var(--white);
    border-radius: 50%;
  }
  .brand__name {
    font-family: "Montserrat", sans-serif;
    font-weight: 500;
    font-size: 24px;
    letter-spacing: 4px;
    color: var(--white);
    text-transform: uppercase;
    white-space: nowrap;
  }
  .badge {
    position: absolute;
    left: 458px;
    top: 132px;
    width: 208px;
    height: 208px;
    border-radius: 50%;
    display: flex;
    align-items: center;
    justify-content: center;
    text-align: center;
    font-family: "Poppins", sans-serif;
    font-weight: 700;
    font-size: 20px;
    line-height: 1.2;
    color: var(--white);
  }
  .cover--deals .badge { background: var(--deals-badge); }
  .cover--reviews .badge { background: var(--reviews-badge); }

  .fine-print {
    position: absolute;
    top: 441px;
    font-family: "Montserrat", sans-serif;
    font-weight: 600;
    font-size: 10px;
    letter-spacing: 0.9px;
    color: var(--fine-print);
    text-transform: uppercase;
    white-space: nowrap;
  }
  .cover--deals .fine-print { right: 374px; }
  .cover--reviews .fine-print { right: 346px; }
</style>
</head>
<body>
<main class="board">

  <section class="cover cover--deals">
    <svg class="cover__scene" viewBox="0 0 877 483">
      <defs>
        <linearGradient id="sand-deals" x1="0" y1="0" x2="1" y2="1">
          <stop offset="0" stop-color="var(--sand-light)"/>
          <stop offset="1" stop-color="var(--sand-dark)"/>
        </linearGradient>
      </defs>
      <path d="M650,0 Q552,210 562,483 L877,483 L877,0 Z" fill="var(--white)"/>
      <path role="img" aria-label="Photo of sand with scattered seashells and a red starfish" d="M658,0 Q562,210 572,483 L877,483 L877,0 Z" fill="url(#sand-deals)"/>
    </svg>
    <div class="brand">
      <span class="brand__dot"></span>
      <span class="brand__name">Gluten Cove</span>
    </div>
    <div class="badge">Travel Deals</div>
    <p class="fine-print">Powered by Journey Crest</p>
  </section>

  <section class="cover cover--reviews">
    <svg class="cover__scene" viewBox="0 0 877 483">
      <defs>
        <linearGradient id="sand-reviews" x1="0" y1="0" x2="1" y2="1">
          <stop offset="0" stop-color="var(--sand-light)"/>
          <stop offset="1" stop-color="var(--sand-dark)"/>
        </linearGradient>
      </defs>
      <path d="M650,0 Q552,210 562,483 L877,483 L877,0 Z" fill="var(--white)"/>
      <path role="img" aria-label="Photo of sand with scattered seashells and a red starfish" d="M658,0 Q562,210 572,483 L877,483 L877,0 Z" fill="url(#sand-reviews)"/>
    </svg>
    <div class="brand">
      <span class="brand__dot"></span>
      <span class="brand__name">Gluten Cove</span>
    </div>
    <div class="badge">All Inclusive<br>Reviews</div>
    <p class="fine-print">Powered by 2 Brightway travel agents</p>
  </section>

</main>
</body>
</html>
```